New locally owned rental company needs a flyer to circulate

Need flyer with logo, phone# and address. We rent cars to anyone with driver's license and proper insurance. Rates as low as $50/day. Can offer compact cars, mid-size and full size sedans. Also SUV's.

```html
<!DOCTYPE html>
<html lang="en">
<head>
<meta charset="utf-8">
<title>DriveReady Car &amp; Van Rental Flyer</title>
<link href="https://fonts.googleapis.com/css2?family=Archivo+Black&family=Barlow:wght@400;600;700;800&display=swap" rel="stylesheet">
<style>
  :root{
    --stage:#e9e9e9;
    --white:#f7f7f7;
    --blue:#0a55ad;
    --green:#2bb34f;
    --charcoal:#3b3b3b;
    --charcoal-deep:#242424;
    --ink:#111111;
    --red:#e81c24;
    --car-red:#c8202b;
    --car-red-dark:#8e141c;
    --text-light:#f2f2f2;
  }
  *{box-sizing:border-box;margin:0;padding:0}
  html,body{width:1200px;height:1080px;overflow:hidden;background:var(--stage)}
  .flyer-frame{position:absolute;left:198px;top:20px;width:1052px;height:1360px;transform:scale(.7647);transform-origin:0 0}
  .flyer{position:relative;width:1052px;height:1360px;background:var(--white);overflow:hidden;font-family:"Barlow",sans-serif;box-shadow:0 10px 30px rgba(0,0,0,.25)}
  .backdrop{position:absolute;inset:0}

  .brand{position:absolute;top:70px;left:0;width:100%;text-align:center}
  .brand-name{display:inline-flex;align-items:center;gap:16px;font-family:"Barlow",sans-serif;font-weight:800;font-size:94px;line-height:1;color:var(--blue);letter-spacing:-1px}
  .brand-mark{width:32px;height:32px;background:var(--green)}
  .brand-tagline{margin-top:12px;font-family:"Archivo Black",sans-serif;font-size:36px;letter-spacing:11px;color:var(--ink)}

  .hero-photo{position:absolute;left:100px;top:272px;width:836px;height:356px;border-radius:28px;background:linear-gradient(160deg,var(--car-red) 0%,#b01a24 55%,var(--car-red-dark) 100%)}

  .eligibility{position:absolute;left:80px;top:642px;color:var(--text-light)}
  .eligibility-intro{font-size:38px;font-weight:400;margin-left:2px}
  .eligibility-item{display:flex;align-items:center;gap:14px;margin-top:6px;font-family:"Barlow",sans-serif;font-weight:700;font-size:52px;line-height:1.15;letter-spacing:-.5px}
  .eligibility-item small{font-weight:600;font-size:36px}

  .price-card{position:absolute;left:645px;top:548px;width:340px;height:306px;background:#fff;transform:rotate(2deg);box-shadow:0 6px 18px rgba(0,0,0,.35);padding:12px}
  .price-card-inner{width:100%;height:100%;border:3px solid var(--blue);text-align:center;padding-top:56px}
  .price-label{font-family:"Barlow",sans-serif;font-weight:800;font-size:24px;color:var(--ink)}
  .price-amount{font-family:"Barlow",sans-serif;font-weight:800;font-size:158px;line-height:.95;color:var(--red);letter-spacing:-6px;margin-top:4px;text-shadow:0 4px 8px rgba(0,0,0,.3)}
  .price-unit{display:block;text-align:right;padding-right:40px;font-family:"Barlow",sans-serif;font-weight:800;font-size:26px;color:var(--red)}

  .fleet-list{position:absolute;left:80px;top:902px;display:flex;gap:16px;list-style:none;font-family:"Barlow",sans-serif;font-weight:700;font-size:28px;color:var(--text-light)}
  .fleet-list li{display:flex;align-items:center;gap:12px}
  .fleet-list li::before{content:"";width:12px;height:12px;border:3px solid var(--blue);background:#fff;border-radius:3px}

  .fleet-photos{position:absolute;left:74px;top:967px;display:flex;gap:6px}
  .fleet-photo{width:298px;height:170px;border:3px solid var(--blue);background:linear-gradient(180deg,#d9c6a4 0%,#9ea3a8 22%,#6c7076 55%,#5a5c60 100%)}
  .fleet-photo.sedan{background:linear-gradient(180deg,#d6c09b 0%,#8e939c 22%,#3d44a6 52%,#52555b 100%)}
  .fleet-photo.suv-silver{background:linear-gradient(180deg,#dcc8a6 0%,#b4b7bb 30%,#9a9da1 60%,#6e7175 100%)}

  .lot-photo{position:absolute;left:0;top:1138px;width:1052px;height:120px;background:linear-gradient(180deg,#4a4a4a 0%,#2e2e2e 100%)}

  .contact{position:absolute;left:84px;top:1180px;width:900px;display:flex;align-items:center;color:var(--text-light)}
  .contact-phone{display:flex;align-items:center;gap:20px;font-family:"Barlow",sans-serif;font-weight:700;font-size:64px;letter-spacing:-1px}
  .contact-address{display:flex;align-items:center;gap:20px;margin-left:66px;font-family:"Barlow",sans-serif;font-weight:600;font-size:24px;line-height:1.25}
  .contact-address address{font-style:normal}
</style>
</head>
<body>
<div class="flyer-frame">
  <div class="flyer">
    <svg class="backdrop" width="1052" height="1360" viewBox="0 0 1052 1360" aria-hidden="true">
      <rect x="0" y="280" width="1052" height="1080" fill="var(--charcoal)"/>
      <polygon points="0,285 1052,200 1052,322 0,398" fill="var(--blue)"/>
      <polygon points="0,398 1052,312 1052,425 0,505" fill="var(--green)"/>
      <polygon points="0,878 1052,806 1052,1360 0,1360" fill="var(--charcoal-deep)"/>
      <polygon points="0,1003 80,995 80,1110 0,1115" fill="var(--green)"/>
      <polygon points="0,1330 588,1282 594,1360 0,1360" fill="var(--blue)"/>
      <polygon points="588,1306 1052,1270 1052,1360 594,1360" fill="var(--green)"/>
    </svg>

    <header class="brand">
      <div class="brand-name"><span>DriveReady</span><span class="brand-mark"></span></div>
      <div class="brand-tagline">Car &amp; Van Rental</div>
    </header>

    <div class="hero-photo" role="img" aria-label="Photo of a red compact sedan from the rental fleet"></div>

    <section class="eligibility">
      <p class="eligibility-intro">We rent cars to anyone with</p>
      <p class="eligibility-item">
        <svg width="42" height="46" viewBox="0 0 42 46" aria-hidden="true"><rect x="3" y="12" width="28" height="30" fill="#fff" stroke="#555" stroke-width="3"/><path d="M8 26 L16 36 L38 4" fill="none" stroke="var(--blue)" stroke-width="6" stroke-linecap="round"/></svg>
        <span>DRIVER'S LICENSE <small>&amp;</small></span>
      </p>
      <p class="eligibility-item">
        <svg width="42" height="46" viewBox="0 0 42 46" aria-hidden="true"><rect x="3" y="12" width="28" height="30" fill="#fff" stroke="#555" stroke-width="3"/><path d="M8 26 L16 36 L38 4" fill="none" stroke="var(--blue)" stroke-width="6" stroke-linecap="round"/></svg>
        <span>PROPER INSURANCE</span>
      </p>
    </section>

    <aside class="price-card">
      <div class="price-card-inner">
        <p class="price-label">RATES AS LOW AS</p>
        <p class="price-amount">$50</p>
        <span class="price-unit">/DAY</span>
      </div>
    </aside>

    <ul class="fleet-list">
      <li>COMPACT CARS</li>
      <li>MID-SIZE SEDANS</li>
      <li>FULL SIZE SEDANS</li>
      <li>SUV</li>
    </ul>

    <div class="fleet-photos">
      <div class="fleet-photo" role="img" aria-label="Photo of a grey SUV parked on the lot"></div>
      <div class="fleet-photo sedan" role="img" aria-label="Photo of a blue sedan parked on the lot"></div>
      <div class="fleet-photo suv-silver" role="img" aria-label="Photo of a silver SUV parked on the lot"></div>
    </div>

    <div class="lot-photo" role="img" aria-label="Faded photo of a row of rental cars"></div>

    <footer class="contact">
      <div class="contact-phone">
        <svg width="46" height="46" viewBox="0 0 24 24" aria-hidden="true"><path fill="var(--blue)" d="M6.6 10.8a15.1 15.1 0 0 0 6.6 6.6l2.2-2.2a1 1 0 0 1 1-.25 11.4 11.4 0 0 0 3.6.57 1 1 0 0 1 1 1V20a1 1 0 0 1-1 1A17 17 0 0 1 3 4a1 1 0 0 1 1-1h3.5a1 1 0 0 1 1 1c0 1.25.2 2.45.57 3.57a1 1 0 0 1-.25 1z"/></svg>
        <span>555-014-2280</span>
      </div>
      <div class="contact-address">
        <svg width="34" height="44" viewBox="0 0 24 32" aria-hidden="true"><path d="M12 2a9 9 0 0 0-9 9c0 7 9 18 9 18s9-11 9-18a9 9 0 0 0-9-9z" fill="#fff" stroke="var(--blue)" stroke-width="3"/><circle cx="12" cy="11" r="3.4" fill="var(--blue)"/></svg>
        <address>4870 Oakline Avenue<br>Riverton, AL 35000</address>
      </div>
    </footer>
  </div>
</div>
</body>
</html>
```